MOLVT Study flyer

I need help designing a flyer for a research study that will include brain imaging in adolescents. The info is in the attached document. The study is called the Marrowby Orchard Lantern Vesper Trail (MOLVT) study. Ideally this would be returned as a document that I can edit in the future as we will have several new recruitment phases (different age groups, etc. I also would love to have a logo designed as part of this project, but I recognize that might be a separate design request.

```html
<!DOCTYPE html>
<html lang="en">
<head>
<meta charset="utf-8">
<title>MOLVT Study Flyer</title>
<link href="https://fonts.googleapis.com/css2?family=Poppins:wght@400;600;700&family=Libre+Franklin:wght@400&display=swap" rel="stylesheet">
<style>
  :root {
    --page-bg: #dedede;
    --paper: #ffffff;
    --brand-blue: #1a4a9e;
    --band-blue: rgba(98, 112, 190, 0.85);
    --gold: #fbb719;
    --cream: #fdebcd;
    --ink: #1d1d1f;
    --body-ink: #2b2b2b;
    --dots: #c9c6c0;
  }
  * { box-sizing: border-box; margin: 0; padding: 0; }
  html, body { width: 881px; height: 1200px; overflow: hidden; background: var(--page-bg); }
  .flyer {
    position: absolute; left: 76px; top: 84px; width: 729px; height: 1031px;
    background: var(--paper); overflow: hidden;
    font-family: "Libre Franklin", Arial, sans-serif; color: var(--body-ink);
  }
  .hero { position: absolute; left: 0; top: 0; width: 729px; height: 470px; }
  .hero svg { position: absolute; inset: 0; }
  .university-name {
    position: absolute; left: 498px; top: 50px; width: 170px;
    font-family: "Poppins", sans-serif; font-weight: 600; font-size: 17px; line-height: 1.15;
    color: #ffffff;
  }
  .headline {
    position: absolute; left: 51px; top: 306px;
    font-family: "Poppins", sans-serif; font-weight: 700; font-size: 29px; line-height: 35px;
    letter-spacing: -0.4px; color: #ffffff;
  }
  .headline .accent { color: var(--gold); display: block; }
  .badge-ring {
    position: absolute; left: 472px; top: 256px; width: 230px; height: 230px;
    border-radius: 50%; background: var(--paper);
  }
  .badge {
    position: absolute; left: 500px; top: 283px; width: 174px; height: 174px;
    border-radius: 50%; background: var(--gold);
    display: flex; flex-direction: column; justify-content: center; padding-left: 20px;
    font-family: "Poppins", sans-serif; font-weight: 400; font-size: 50px; line-height: 44px;
    color: var(--brand-blue);
  }
  .badge-arrow { position: absolute; left: 576px; top: 445px; }
  .details { position: absolute; left: 0; top: 470px; width: 729px; height: 135px; background: var(--cream); }
  .details-row {
    position: absolute; left: 75px; width: 580px; height: 48px;
    display: flex; align-items: center;
    font-family: "Poppins", sans-serif; font-size: 18px; color: var(--ink);
    border-bottom: 2px dotted var(--dots);
  }
  .details-row.first { border-top: 2px dotted var(--dots); top: 20px; }
  .details-row.second { top: 70px; }
  .details-row dt { width: 152px; padding-left: 3px; font-weight: 700; }
  .details-row dd { font-weight: 400; }
  .section-title {
    font-family: "Poppins", sans-serif; font-weight: 700; font-size: 17.5px;
    color: var(--brand-blue); letter-spacing: -0.2px;
  }
  .intro { position: absolute; left: 75px; top: 649px; width: 210px; }
  .intro p { margin-top: 20px; font-size: 14.5px; line-height: 17.7px; }
  .contact { position: absolute; left: 75px; top: 847px; width: 203px; list-style: none; border-top: 2px dotted var(--dots); }
  .contact li {
    height: 34px; display: flex; align-items: center; gap: 6px;
    font-family: "Poppins", sans-serif; font-size: 12px; border-bottom: 2px dotted var(--dots);
  }
  .contact b { color: var(--brand-blue); font-weight: 700; }
  .details-col { position: absolute; left: 317px; top: 648px; width: 345px; font-size: 12.3px; line-height: 14.7px; }
  .details-col ul { list-style: none; margin: 15px 0 0; }
  .details-col li { position: relative; padding-left: 22px; }
  .details-col li::before { content: "•"; position: absolute; left: 1px; top: 0; }
  .details-col .section-title.second { margin-top: 17px; }
  .details-col p { margin-top: 15px; }
  .details-col p.compensation { margin-top: 14px; }
</style>
</head>
<body>
<main class="flyer">
  <section class="hero">
    <svg width="729" height="470" viewBox="0 0 729 470">
      <defs>
        <linearGradient id="panelLeft" x1="0" y1="0" x2="1" y2="1">
          <stop offset="0" stop-color="#e7c9b2"/><stop offset="1" stop-color="#b89a84"/>
        </linearGradient>
        <linearGradient id="panelMid" x1="0" y1="0" x2="0" y2="1">
          <stop offset="0" stop-color="#f3f1ee"/><stop offset="0.5" stop-color="#b9cfe0"/><stop offset="1" stop-color="#3e5678"/>
        </linearGradient>
        <linearGradient id="panelRight" x1="0" y1="0" x2="1" y2="1">
          <stop offset="0" stop-color="#c9a892"/><stop offset="1" stop-color="#e8d6c6"/>
        </linearGradient>
      </defs>
      <g role="img" aria-label="Photographs of three teenage girls looking thoughtful">
        <polygon points="0,0 121,0 290,470 0,470" fill="url(#panelLeft)"/>
        <polygon points="131,0 449,0 622,470 300,470" fill="url(#panelMid)"/>
        <polygon points="459,0 729,0 729,470 632,470" fill="url(#panelRight)"/>
      </g>
      <polygon points="116,0 127,0 296,470 285,470" fill="#fbb719"/>
      <polygon points="444,0 455,0 628,470 617,470" fill="#fbb719"/>
      <rect x="0" y="288" width="729" height="182" fill="rgba(98,112,190,0.85)"/>
    </svg>
    <div class="university-name">Alderbrook<br>University</div>
    <h1 class="headline">Are you the parent<br>of a child age 10–17?<span class="accent">Do they worry or overthink<br>negative emotions?</span></h1>
    <div class="badge-ring"></div>
    <div class="badge"><span>Case</span><span>Study</span></div>
    <svg class="badge-arrow" width="22" height="22" viewBox="0 0 22 22">
      <circle cx="11" cy="11" r="11" fill="#ffffff"/>
      <circle cx="11" cy="11" r="8.5" fill="#fbb719"/>
      <path d="M11 6.5v8M7.5 11.5l3.5 3.5 3.5-3.5" fill="none" stroke="#1a4a9e" stroke-width="1.3" stroke-linecap="round"/>
    </svg>
  </section>

  <section class="details">
    <dl>
      <div class="details-row first"><dt>Project Name:</dt><dd>Project Name</dd></div>
      <div class="details-row second"><dt>Timeline:</dt><dd>Project completion 2 weeks</dd></div>
    </dl>
  </section>

  <section class="intro">
    <h2 class="section-title">If your answernis YES:</h2>
    <p>The Alderbrook University researchers are seeking girls age 10-17 for a study about brain activity in emotions and decision-making and how they relate to puberty, anxiety and depression.</p>
  </section>

  <ul class="contact">
    <li><b>P:</b> +1 555 0142 7781</li>
    <li><b>E:</b> molvtstudy@alderbrookhealth.org</li>
    <li><b>W:</b> alderbrookhealth.org</li>
  </ul>

  <section class="details-col">
    <h2 class="section-title">Study participation involves:</h2>
    <ul>
      <li>One one-hour interview (online or in-person) where your child will discuss their thoughts</li>
      <li>Online questionnaires (parent and child)</li>
      <li>One two-hour visit where your child will complete an MRI scan, answer questions about their puberty stage, and have a small hair sample taken to study puberty hormones</li>
    </ul>
    <h2 class="section-title second">Your child may be eligible if they:</h2>
    <ul>
      <li>Are age 10-17</li>
      <li>Tend to worry or overthink negative thoughts</li>
      <li>have not been diagnosed with psychosis, learning problems, or autism</li>
    </ul>
    <p>Interested in participating? Want more information? Please contact us! molvtstudy@alderbrookhealth.org</p>
    <p class="compensation">Compensation up to $140</p>
  </section>
</main>
</body>
</html>
```